HIGH END MEDICAL/ANTI-AGING START-UP BROCHURE + BUSINESS CARDS

Fernridgewellnessco.example needs a brochure which details our two top selling products. The Vital Matrix Profile Review (VMP) coupled with the 4(16) Plan.

Here is some information about the VMP and the 4(16) plan. Please see our website for pictures and color.

VMP-Vital Matrix Profile and Fernridge
Fernridge Wellness Co is changing the way people look at health by bringing the focus back to the physical examination and patient centered care. It's our new, cutting edge system, Vital Matrix Profile, that allows us to have unparalleled patient outcomes. Vital Matrix Profile is a true deep dive into the individual. The protocol assesses, measures and tracking over 70 different bio-parameters such as hormone balance, tissue health, muscle mass, fat mass, frame mass, water content, water distribution, and acid/alkaline balance. This new analytics tool allows hyper individualized and customized weight loss and health programs to evolve in a new and never before seen way.

The 4(16) Plan
The 4(16) Cleanse plan works by creating a full metabolic reset geared towards facilitation of hormone optimization and balance as well as toxicity and fat removal. Toxins are fat soluble and often need targeted nutritional strategy for long-term weight loss to occur; this is why many people do not lose weight even on calorie restricted diets with exercise plans until they use proper nutritional protocol. The 4(16) Cleanse allows for fat cells to be released and disposed of while at the same time adding deficient nutrients back into the tissues, helping you to not only lose weight, but reach optimal health and hormonal balance at the same time.

Target Market(s)

High-end and upscale clients looking for boutique medical services. We deal with clients mostly in executive level finance.

Industry/Entity Type

Medical

Contact Information for Business Card

-Must have our logo
-website (fernridgewellnessco.example)
-a space for our titles, "Dr. Anton Pelsing, Founder" & "Rosalind Pelsing, Program Director"
-office phone number and our cell phone numbers (we will give you our cell phone numbers later)

Font styles to use
Serif
Sans Serif

Colors
0355a3
0493ce
00a990
ffffff
000000
919191
474747

Requirements
Must have
• Brochure and business cards must be VERY modern, creative and sophisticated.
Nice to have
• Usage of the company colors and logo in a new and interesting way.
Should not have
• Do not use colors outside of our logo + black + grey or white.
• Nothing cartoonish.

```html
<!DOCTYPE html>
<html lang="en">
<head>
<meta charset="utf-8">
<title>Fernridge Wellness Co – Tri-fold Brochure</title>
<link rel="stylesheet" href="https://fonts.googleapis.com/css2?family=Open+Sans:wght@300;400;600;700&display=swap">
<style>
  :root {
    --page-bg: #e6e6e6;
    --brand-teal: #00a990;
    --brand-navy: #0355a3;
    --brand-sky: #0493ce;
    --paper: #f2f2f2;
    --white: #ffffff;
    --grey: #919191;
    --grey-dark: #474747;
    --line-soft: rgba(255, 255, 255, 0.55);
  }
  * { box-sizing: border-box; margin: 0; padding: 0; }
  html, body {
    width: 1200px; height: 800px; overflow: hidden;
    background: var(--page-bg);
    font-family: "Open Sans", Arial, sans-serif;
  }
  .brochure {
    position: absolute; left: 90px; top: 30px;
    width: 1020px; height: 740px;
    display: flex;
    box-shadow: 0 10px 30px rgba(0,0,0,0.18);
  }
  .panel { position: relative; width: 340px; height: 740px; overflow: hidden; }

  /* Inside info panel */
  .panel--info {
    background: var(--brand-teal);
    color: var(--white);
    padding: 40px 32px 30px;
  }
  .info-heading {
    font-size: 17px; font-weight: 700; letter-spacing: 0.2px;
    text-transform: uppercase; line-height: 1.2;
  }
  .info-heading .light { font-weight: 300; }
  .info-rule { height: 1px; background: var(--line-soft); margin: 6px 0 10px; }
  .info-copy {
    font-size: 9.4px; line-height: 1.5; font-weight: 400;
    text-align: justify; margin-bottom: 22px;
  }
  .info-subheading {
    font-size: 13.5px; font-weight: 600; line-height: 1.3;
  }

  /* Middle + cover share one background drawing */
  .spread-art {
    position: absolute; left: 340px; top: 0;
    width: 680px; height: 740px;
  }
  .panel--contact, .panel--cover { background: transparent; }

  .contact-list {
    position: absolute; left: 46px; top: 470px; right: 20px;
    list-style: none; color: var(--white);
    font-size: 12.5px; line-height: 1.35;
  }
  .contact-list li { display: flex; align-items: flex-start; margin-bottom: 14px; }
  .contact-list li.tight { margin-bottom: 6px; }
  .contact-list svg { flex: none; width: 14px; height: 14px; margin: 2px 12px 0 0; }

  .brand-mark {
    position: absolute; top: 58px; left: 0; right: 0;
    display: flex; flex-direction: column; align-items: center; gap: 12px;
  }
  .brand-mark__dot {
    width: 54px; height: 54px; border-radius: 50%;
    background: var(--brand-teal);
  }
  .brand-mark__name {
    font-size: 19px; font-weight: 700; color: var(--brand-navy);
    letter-spacing: 1.5px; text-transform: uppercase;
  }

  .plan-block {
    position: absolute; left: 32px; right: 32px; top: 490px;
    color: var(--white);
  }
  .plan-block .info-heading { font-size: 15px; }
  .plan-block .info-copy { margin-bottom: 0; }

  .cover-url {
    position: absolute; right: 30px; bottom: 30px;
    color: var(--white); font-size: 12.5px; font-weight: 600;
  }
</style>
</head>
<body>
<main class="brochure">

  <section class="panel panel--info">
    <h2 class="info-heading">VMP-Vital Matrix <span class="light">Profile</span></h2>
    <div class="info-rule"></div>
    <p class="info-copy">Fernridge Wellness Co is changing the way people look at health by bringing the focus back to the physical examination and patient centered care. It's our new, cutting edge system, Vital Matrix Profile, that allows us to have unparalleled patient outcomes. Vital Matrix Profile is a true deep dive into the individual. The protocol assesses, measures and tracking over 70 different bio-parameters such as hormone balance, tissue health, muscle mass, fat mass, frame mass, water content, water distribution, and acid/alkaline balance. This new analytics tool allows hyper individualized and customized weight loss and health programs to evolve in a new and never before seen way.</p>

    <h2 class="info-heading">Leanness &amp; Health</h2>
    <div class="info-rule"></div>
    <p class="info-copy">The scientific community has held lean body composition as one of the 4 tenets in maintaining good health for decades. Yet, we are the fattest nation in the world. The weight loss industry is booming and failing all in the same time. Lifestyle diseases are taking over our healthcare system with no definitive forms of treatment while at the same time, expensive drugs are failing our families, communities and nation. Why? The answer is lack of an effective way to assess, track and treat body composition. The better your body composition and cellular health is, the better you feel the better you look, and the better you can be a role model for those you care about. It might be considered vain to want to look great! If that's the case, then we at Fernridge Wellness Co are 100% OK with that. Whatever your reason for changing your body composition, weight loss, health or vanity, we're on board!</p>

    <div class="info-rule"></div>
    <h3 class="info-subheading">Being Lean for Health<br>and Vanity =’s Healthy Vanity!</h3>
    <p class="info-copy" style="margin-top:8px">Dr. Anton has coined the term “healthy vanity” to popularize the realization that looking and feeling good are often one in the same, that we shouldn't feel guilty for making and wanting our insides, and our outsides, to be healthy as well as aesthetically pleasing.</p>
  </section>

  <svg class="spread-art" viewBox="0 0 680 740">
    <defs>
      <linearGradient id="torso-tones" x1="0" y1="0" x2="1" y2="1">
        <stop offset="0" stop-color="#2a1a14"/>
        <stop offset="0.45" stop-color="#6a4030"/>
        <stop offset="1" stop-color="#140e0c"/>
      </linearGradient>
      <linearGradient id="portrait-tones" x1="0" y1="0" x2="1" y2="1">
        <stop offset="0" stop-color="#8cb24a"/>
        <stop offset="0.5" stop-color="#c99a7c"/>
        <stop offset="1" stop-color="#3f6b2a"/>
      </linearGradient>
      <linearGradient id="map-tones" x1="0" y1="0" x2="0" y2="1">
        <stop offset="0" stop-color="#e8e4da"/>
        <stop offset="1" stop-color="#a9c6ec"/>
      </linearGradient>
    </defs>

    <!-- contact panel -->
    <rect x="0" y="0" width="340" height="740" fill="var(--brand-teal)"/>
    <path d="M0,300 Q170,372 340,430 L340,446 Q170,388 0,318 Z" fill="var(--brand-navy)"/>
    <path role="img" aria-label="Photo of a toned midriff" d="M0,0 H340 V430 Q170,372 0,300 Z" fill="url(#torso-tones)"/>

    <!-- cover panel -->
    <rect x="340" y="0" width="340" height="740" fill="var(--brand-teal)"/>
    <path d="M340,446 Q510,450 680,378 L680,394 Q510,466 340,462 Z" fill="var(--brand-navy)"/>
    <path role="img" aria-label="Photo of a woman holding fresh vegetables" d="M340,200 Q510,196 680,146 V378 Q510,450 340,446 Z" fill="url(#portrait-tones)"/>
    <path d="M340,0 H680 V146 Q510,196 340,200 Z" fill="var(--paper)"/>
    <path d="M340,200 Q510,196 680,146" fill="none" stroke="var(--brand-teal)" stroke-width="1.2"/>

    <!-- location map -->
    <circle cx="135" cy="352" r="80" fill="var(--brand-navy)"/>
    <circle role="img" aria-label="Map of the office location" cx="135" cy="352" r="72" fill="url(#map-tones)"/>
  </svg>

  <section class="panel panel--contact">
    <ul class="contact-list">
      <li>
        <svg viewBox="0 0 14 14"><path d="M7 1a4 4 0 0 1 4 4c0 3-4 7-4 7S3 8 3 5a4 4 0 0 1 4-4z" fill="none" stroke="#fff" stroke-width="1.3"/><circle cx="7" cy="5" r="1.4" fill="#fff"/></svg>
        <span>Fernridge Wellness Co<br>218 Alder Row Suite 40<br>Brookvale CT, 06999</span>
      </li>
      <li>
        <svg viewBox="0 0 14 14"><path d="M7 1a4 4 0 0 1 4 4c0 3-4 7-4 7S3 8 3 5a4 4 0 0 1 4-4z" fill="none" stroke="#fff" stroke-width="1.3"/><circle cx="7" cy="5" r="1.4" fill="#fff"/></svg>
        <span>Eastmere Office:<br>77 Harbor Lane<br>Eastmere, NY, 10999</span>
      </li>
      <li class="tight">
        <svg viewBox="0 0 14 14"><rect x="1.5" y="3" width="11" height="8" fill="none" stroke="#fff" stroke-width="1.2"/><path d="M1.5 3l5.5 4.5L12.5 3" fill="none" stroke="#fff" stroke-width="1.2"/></svg>
        <span>Info@Fernridgewellnessco.example</span>
      </li>
      <li class="tight">
        <svg viewBox="0 0 14 14"><path d="M3 1.5l2 2.5-1.2 1.5a8 8 0 0 0 4.7 4.7L10 9l2.5 2-1.3 1.8C6.5 12.5 1.5 7.5 1.2 2.8z" fill="none" stroke="#fff" stroke-width="1.2"/></svg>
        <span>(555) 014-2290</span>
      </li>
      <li class="tight">
        <svg viewBox="0 0 14 14"><circle cx="7" cy="7" r="5.5" fill="none" stroke="#fff" stroke-width="1.2"/><ellipse cx="7" cy="7" rx="2.3" ry="5.5" fill="none" stroke="#fff" stroke-width="1"/><path d="M1.5 7h11" stroke="#fff" stroke-width="1"/></svg>
        <span>www.fernridgewellnessco.example</span>
      </li>
    </ul>
  </section>

  <section class="panel panel--cover">
    <div class="brand-mark">
      <span class="brand-mark__dot"></span>
      <span class="brand-mark__name">Fernridge Wellness Co</span>
    </div>
    <div class="plan-block">
      <h2 class="info-heading">The 4(16) <span class="light">Plan</span></h2>
      <div class="info-rule"></div>
      <p class="info-copy">The 4(16) Cleanse plan works by creating a full metabolic reset geared towards hormone optimization and balance as well as toxicity and fat removal. Toxins are fat soluble and often need a targeted nutritional strategy for long-term weight loss to occur. The 4(16) Cleanse allows fat cells to be released and disposed of while adding deficient nutrients back into the tissues, helping you not only lose weight, but reach optimal health and hormonal balance at the same time.</p>
    </div>
    <p class="cover-url">www.fernridgewellnessco.example</p>
  </section>

</main>
</body>
</html>
```